Bright Fern Custom Homes business card. Double sided. Modern. professional

Bright Fern Custom Homes
contemporary modern design with our logo /
Double sided with all our contact information
Use same Green colors as in our Logo. Contemporary logo that grabs your attention. Visually pleasing and balanced. Easy to read, and Vibrant. Would love an option for rounded edges. Embossed logo would be amazing.
Contact Information for Business Card
Dana Welk Owner / General Contractor Bright Fern Custom Homes p: 704.552.1830 m: 912.648.2071 e: brightferncustomhomes@mailbox.example w: www.brightferncustomhomes.example 218 Pryor Meadow Lane Batesburg, SC 29041

```html
<!DOCTYPE html>
<html lang="en">
<head>
<meta charset="utf-8">
<title>Bright Fern Custom Homes – Business Card</title>
<link rel="stylesheet" href="https://fonts.googleapis.com/css2?family=Arimo:wght@400;700&display=swap">
<style>
  :root {
    --backdrop: #e2e2e2;
    --card-white: #ffffff;
    --card-black: #070a0b;
    --green-dark: #5a7130;
    --green-light: #7a9339;
    --green-text: #6a7f34;
    --ink: #1b1b1b;
  }
  * { box-sizing: border-box; margin: 0; padding: 0; }
  html, body {
    width: 1200px; height: 1200px; overflow: hidden;
    background: var(--backdrop);
    font-family: "Arimo", Arial, sans-serif;
  }
  .canvas { position: relative; width: 1200px; height: 1200px; }
  .card {
    position: absolute;
    width: 825px; height: 474px;
    border-radius: 26px;
    overflow: hidden;
  }
  .card--front { left: 188px; top: 91px; background: var(--card-white); }
  .card--back { left: 187px; top: 636px; background: var(--card-black); }

  .wave { position: absolute; left: 0; top: 0; width: 825px; height: 474px; }

  .brand {
    position: absolute;
    display: flex; flex-direction: column; align-items: center;
    color: var(--green-text);
    font-weight: 700;
    text-align: center;
  }
  .brand__mark { border-radius: 50%; background: var(--green-dark); }
  .card--front .brand { left: 40px; top: 118px; width: 324px; }
  .card--front .brand__mark { width: 118px; height: 118px; margin-bottom: 24px; }
  .card--front .brand__name { font-size: 30px; letter-spacing: 1px; line-height: 1.1; }
  .card--front .brand__sub { font-size: 11px; letter-spacing: 7px; margin-top: 4px; }

  .card--back .brand { left: 0; top: 90px; width: 825px; }
  .card--back .brand__mark { width: 190px; height: 190px; margin-bottom: 34px; }
  .card--back .brand__name { font-size: 46px; letter-spacing: 2px; line-height: 1.1; }
  .card--back .brand__sub { font-size: 15px; letter-spacing: 10px; margin-top: 6px; }

  .divider {
    position: absolute; left: 393px; top: 120px;
    width: 2px; height: 236px; background: var(--green-dark);
  }
  .contact { position: absolute; left: 429px; top: 112px; color: var(--ink); }
  .contact__name {
    font-size: 31px; font-weight: 700; color: var(--green-text);
    letter-spacing: 0.3px; line-height: 1.1;
  }
  .contact__role { font-size: 19px; margin-top: 4px; }
  .contact__address { font-size: 19px; line-height: 26px; margin-top: 18px; }
  .contact__list { list-style: none; margin-top: 18px; }
  .contact__item {
    display: flex; align-items: center; gap: 10px;
    font-size: 19px; height: 26.5px;
  }
  .contact__icon { width: 18px; height: 18px; flex: none; fill: var(--green-dark); }
</style>
</head>
<body>
<main class="canvas">

  <section class="card card--front" aria-label="Business card front">
    <svg class="wave" viewBox="0 0 825 474" aria-hidden="true">
      <path d="M0 398 C 170 372 330 378 480 405 C 600 428 690 455 825 420 L825 474 L0 474 Z" fill="var(--green-dark)"/>
      <path d="M0 420 C 170 396 330 400 480 422 C 600 440 700 456 825 424" fill="none" stroke="#fff" stroke-width="3"/>
      <path d="M0 424 C 170 400 330 404 480 426 C 600 444 700 460 825 428 L825 474 L0 474 Z" fill="var(--green-light)"/>
    </svg>

    <div class="brand">
      <span class="brand__mark" aria-hidden="true"></span>
      <span class="brand__name">BRIGHT FERN</span>
      <span class="brand__sub">CUSTOM HOMES</span>
    </div>

    <div class="divider"></div>

    <div class="contact">
      <h1 class="contact__name">DANA WELK</h1>
      <p class="contact__role">Owner / General Contractor</p>
      <p class="contact__address">218 Pryor Meadow Lane Batesburg<br>SC 29041</p>
      <ul class="contact__list">
        <li class="contact__item">
          <svg class="contact__icon" viewBox="0 0 24 24" aria-hidden="true"><path d="M6.6 10.8a15.1 15.1 0 0 0 6.6 6.6l2.2-2.2a1 1 0 0 1 1-.25 11.4 11.4 0 0 0 3.6.57 1 1 0 0 1 1 1V20a1 1 0 0 1-1 1A17 17 0 0 1 3 4a1 1 0 0 1 1-1h3.5a1 1 0 0 1 1 1c0 1.25.2 2.45.57 3.57a1 1 0 0 1-.25 1z"/></svg>
          704.552.1830
        </li>
        <li class="contact__item">
          <svg class="contact__icon" viewBox="0 0 24 24" aria-hidden="true"><path d="M7 1h10a2 2 0 0 1 2 2v18a2 2 0 0 1-2 2H7a2 2 0 0 1-2-2V3a2 2 0 0 1 2-2zm0 3v15h10V4zm4 16.2h2v1.3h-2z"/></svg>
          912.648.2071
        </li>
        <li class="contact__item">
          <svg class="contact__icon" viewBox="0 0 24 24" aria-hidden="true"><path d="M2 5h20v14H2zm2 2v.5l8 5.5 8-5.5V7l-8 5.5z"/></svg>
          brightferncustomhomes@mailbox.example
        </li>
        <li class="contact__item">
          <svg class="contact__icon" viewBox="0 0 24 24" aria-hidden="true"><path d="M12 2a10 10 0 1 0 0 20 10 10 0 0 0 0-20zm6.9 6h-3a15 15 0 0 0-1.3-3.9A8 8 0 0 1 18.9 8zM12 4c.9 1.2 1.6 2.6 2 4h-4c.4-1.4 1.1-2.8 2-4zM4.3 14a8 8 0 0 1 0-4h3.4a16 16 0 0 0 0 4zm.8 2h3a15 15 0 0 0 1.3 3.9A8 8 0 0 1 5.1 16zm3-8h-3a8 8 0 0 1 4.3-3.9A15 15 0 0 0 8.1 8zM12 20c-.9-1.2-1.6-2.6-2-4h4c-.4 1.4-1.1 2.8-2 4zm2.3-6H9.7a14 14 0 0 1 0-4h4.6a14 14 0 0 1 0 4zm.3 5.9a15 15 0 0 0 1.3-3.9h3a8 8 0 0 1-4.3 3.9zm1.7-5.9a16 16 0 0 0 0-4h3.4a8 8 0 0 1 0 4z"/></svg>
          www.brightferncustomhomes.example
        </li>
      </ul>
    </div>
  </section>

  <section class="card card--back" aria-label="Business card back">
    <div class="brand">
      <span class="brand__mark" aria-hidden="true"></span>
      <span class="brand__name">BRIGHT FERN</span>
      <span class="brand__sub">CUSTOM HOMES</span>
    </div>
  </section>

</main>
</body>
</html>
```